Flyer für Computer Service
Zielgruppe
Privathaushalte und kleinere Firmen.
Wir möchten damit neue Kunden für unsere Dienstleistungen gewinnen.
Aufgabenstellung
Wir möchten mit diesem Flyer speziell unsere Computer Service Dienstleistungen bewerben.
Im wesentlichen werden folgende 3 Kategorieren von Dienstleistungen angeboten:
- Fernwartung
- Reparaturen
- Neuinstallationen, Backups und Virenentfernung
Fernwartung und Reparaturen bieten wir zu "ab EUR xx.-" Preisen an und Neuinstallationen, Backups und Virenentfernung zu Pauschalen.

```html
<!DOCTYPE html>
<html lang="de">
<head>
<meta charset="utf-8">
<title>Relvano – PC Service Flyer</title>
<link href="https://fonts.googleapis.com/css2?family=Open+Sans:wght@400;600;700;800&display=swap" rel="stylesheet">
<style>
:root{
  --orange:#f7931e;
  --orange-light:#fbb040;
  --orange-deep:#e8760a;
  --blue:#1b75bc;
  --blue-light:#3a9ad9;
  --blue-deep:#0d4f8b;
  --dark:#2b2b2b;
  --grey:#4a4a4a;
  --white:#ffffff;
  --ink:#1f2f4a;
}
*{margin:0;padding:0;box-sizing:border-box}
html,body{width:849px;height:1200px;overflow:hidden;background:#fff}
body{font-family:"Open Sans",Arial,sans-serif}
.flyer{position:relative;width:849px;height:1200px;overflow:hidden;background:var(--orange)}
.backdrop{position:absolute;inset:0}
.portrait{position:absolute;left:40px;top:30px;width:220px;height:290px;border-radius:6px;
  background:linear-gradient(180deg,#9cc7e8 0%,#3d4a5a 55%,#1e2630 100%)}
.hardware{position:absolute;left:500px;top:300px;width:330px;height:240px;border-radius:6px;
  background:linear-gradient(135deg,#6a6a6a 0%,#1c1c1c 60%,#3a3a3a 100%)}
.headline{position:absolute;right:36px;top:40px;text-align:right;color:var(--white)}
.headline h1{font-size:50px;font-weight:700;letter-spacing:1px;margin-right:20px}
.headline .sub{font-size:23px;font-weight:700;line-height:1.4;margin-top:14px}
.headline .pitch{font-size:17px;font-weight:600;line-height:1.55;margin-top:24px}
.headline .pitch b{font-size:22px;font-weight:800}
.box{position:absolute;padding:14px 16px;color:var(--ink)}
.box h2{font-size:22px;font-weight:700;letter-spacing:.5px;margin-bottom:14px}
.box p{font-size:13.5px;font-weight:700;line-height:1.32}
.box .price{position:absolute;bottom:14px;font-weight:800;font-size:26px}
.box .price strong{font-size:40px;margin-left:6px}
.box-blue{background:linear-gradient(180deg,var(--blue-light),var(--blue-deep));color:var(--white)}
.box-blue h2{color:var(--orange)}
.box-blue .price{color:var(--white)}
.box-blue .price strong{color:var(--orange)}
.box-orange{background:linear-gradient(180deg,var(--orange-light),var(--orange-deep))}
.box-orange h2{color:var(--ink)}
.box-orange .price{color:var(--ink)}
.box-orange .price strong{color:var(--white)}
.box-light{background:linear-gradient(180deg,#ffffff,#e9e9e9);border:3px solid var(--orange)}
.box-light h2{color:var(--blue-deep)}
.box-light .price{color:var(--blue-deep)}
.box-light .price strong{color:var(--orange)}
.repairs{left:0;top:393px;width:250px;height:290px}
.remote{left:262px;top:393px;width:240px;height:290px}
.install{left:0;top:690px;width:278px;height:285px}
.backups{left:288px;top:690px;width:280px;height:285px;border:3px solid var(--white)}
.virus{left:582px;top:690px;width:267px;height:285px}
.features{position:absolute;left:533px;top:558px;list-style:none;color:var(--white);font-size:21px;font-weight:700;line-height:1.22}
.features li::before{content:"";display:inline-block;width:12px;height:12px;background:var(--orange);border:2px solid var(--white);margin-right:16px;vertical-align:2px}
.footer{position:absolute;left:0;top:982px;width:849px;height:218px}
.brand{position:absolute;left:50px;top:42px;width:330px;height:90px;background:var(--orange);border-radius:6px;
  display:flex;align-items:center;justify-content:center;color:var(--white);font-size:66px;font-weight:800;letter-spacing:2px}
.web{position:absolute;left:268px;top:134px;font-size:19px;font-weight:800;color:var(--white)}
.web span{color:var(--orange)}
.imprint{position:absolute;left:58px;top:170px;font-size:15px;font-weight:700;color:var(--white)}
.contact{position:absolute;left:545px;top:70px;transform:rotate(-12deg);color:var(--white);font-weight:800;text-align:left}
.contact .label{font-size:24px}
.contact .phone{font-size:34px;letter-spacing:1px}
.contact .mail{font-size:16px}
</style>
</head>
<body>
<div class="flyer">
  <svg class="backdrop" width="849" height="1200" viewBox="0 0 849 1200" aria-hidden="true">
    <defs>
      <radialGradient id="sun" cx="0.75" cy="0.1" r="0.8">
        <stop offset="0" stop-color="#fdb94a"/>
        <stop offset="1" stop-color="#f58220"/>
      </radialGradient>
      <linearGradient id="panel" x1="0" y1="0" x2="1" y2="1">
        <stop offset="0" stop-color="#2a8ad6"/>
        <stop offset="1" stop-color="#0d4f8b"/>
      </linearGradient>
      <linearGradient id="band" x1="0" y1="0" x2="0" y2="1">
        <stop offset="0" stop-color="#555"/>
        <stop offset="1" stop-color="#1e1e1e"/>
      </linearGradient>
      <linearGradient id="foot" x1="0" y1="0" x2="1" y2="0">
        <stop offset="0" stop-color="#1b75bc"/>
        <stop offset="1" stop-color="#0d4f8b"/>
      </linearGradient>
    </defs>
    <rect width="849" height="1200" fill="url(#sun)"/>
    <polygon points="0,0 330,0 300,340 0,322" fill="url(#panel)"/>
    <polygon points="0,322 300,340 300,346 0,328" fill="#fff"/>
    <path d="M0 380 L560 380 Q700 330 849 300 L849 690 L0 690 Z" fill="url(#band)"/>
    <path d="M0 378 L560 378 Q700 328 849 298" fill="none" stroke="#fff" stroke-width="4"/>
    <rect x="0" y="682" width="849" height="300" fill="#dcdcdc"/>
    <rect x="0" y="982" width="849" height="218" fill="url(#foot)"/>
    <path d="M520 1200 L560 1040 Q700 1000 849 985 L849 1200 Z" fill="#f7931e"/>
    <path d="M500 1200 L545 1030 Q700 990 849 975" fill="none" stroke="#fff" stroke-width="4"/>
  </svg>

  <div class="portrait" role="img" aria-label="Foto eines Technikers im Anzug mit Laptop unter dem Arm"></div>
  <div class="hardware" role="img" aria-label="Foto von Laptop, PC-Tower, Tastatur und Maus"></div>

  <header class="headline">
    <h1>PC PROBLEME ???</h1>
    <p class="sub">..kein Problem, wir helfen Ihnen Sofort<br>Professinal, Schnell und Günstig</p>
    <p class="pitch">Lassen Sie sich von unserem Fachpersonal <b>Beraten</b><br>und von unseren Profis <b>Helfen</b></p>
  </header>

  <section class="box box-blue repairs">
    <h2>REPERATUREN</h2>
    <p>Hier könnte ihr Feintext stehen der Ihre Leistung genau erklährt. Hier könnte ihr Feintext stehen der Ihre Leistung genau erklährt. Hier könnte ihr Feintext stehen der Ihre Leistung genau erklährt. Hier</p>
    <div class="price">schon ab<strong>89 €</strong></div>
  </section>

  <section class="box box-orange remote">
    <h2>FERNWARTUNG</h2>
    <p>Hier könnte ihr Feintext stehen der Ihre Leistung genau erklährt. Hier könnte ihr Feintext stehen der Ihre Leistung genau erklährt. Hier könnte ihr Feintext stehen der Ihre Leistung genau erklährt. Hier</p>
    <div class="price">schon ab<strong>55 €</strong></div>
  </section>

  <ul class="features">
    <li>Schneller Service</li>
    <li>Fixe Tiefpreise</li>
    <li>Kompetente Beratung</li>
    <li>Professioneller Support</li>
  </ul>

  <section class="box box-orange install">
    <h2>NEUINSTALLATIONEN</h2>
    <p>Hier könnte ihr Feintext stehen der Ihre Leistung genau erklährt. Hier könnte ihr Feintext stehen der Ihre Leistung genau erklährt. Hier könnte ihr Feintext stehen der Ihre Leistung genau erklährt. Hier könnte ihr Feintext</p>
    <div class="price" style="right:40px">nur<strong>39 €</strong></div>
  </section>

  <section class="box box-blue backups">
    <h2>BACKUPS</h2>
    <p>Hier könnte ihr Feintext stehen der Ihre Leistung genau erklährt. Hier könnte ihr Feintext stehen der Ihre Leistung genau erklährt. Hier könnte ihr Feintext stehen der Ihre Leistung genau erklährt. Hier könnte ihr Feintext</p>
    <div class="price" style="right:50px">nur<strong>67 €</strong></div>
  </section>

  <section class="box box-light virus">
    <h2>Virenentfernung</h2>
    <p>Hier könnte ihr Feintext stehen der Ihre Leistung genau erklährt. Hier könnte ihr Feintext stehen der Ihre Leistung genau erklährt. Hier könnte ihr Feintext stehen der Ihre Leistung genau erklährt. Hier könnte ihr Feintext</p>
    <div class="price" style="right:26px">nur<strong>69 €</strong></div>
  </section>

  <footer class="footer">
    <div class="brand">relvano</div>
    <div class="web">www.<span>relvano</span>.de</div>
    <div class="imprint">Relvano GmbH - Lindenweg 8 - Bergfelden 34512</div>
    <div class="contact">
      <div class="label">INFOS UNTER :</div>
      <div class="phone">0800 / 4455667</div>
      <div class="mail">Email : info@relvano.de</div>
    </div>
  </footer>
</div>
</body>
</html>
```